Winter Fence Sale Fence Types

Please create a flyer, similar to what we did previous, but mimicking this page listing the fence styles: http://bramblewoodrails.com/snowfall-deal-2019

Industry/Entity Type

Residential Construction

Font styles to use
Sans Serif

Colors
cee9f5
33a6d7
d0dfed

Requirements
Must have
• Fence styles and photo of fence styles
Nice to have
• Phone number, address, logo

```html
<!DOCTYPE html>
<html lang="en">
<head>
<meta charset="utf-8">
<title>Bramblewood Rails – Winter Fence Sale Flyer</title>
<link rel="stylesheet" href="https://fonts.googleapis.com/css2?family=Montserrat+Alternates:wght@600;700&family=Nunito:wght@400;600;700;800&display=swap">
<style>
  :root{
    --page:#cee9f5;
    --sky:#33a6d7;
    --mist:#d0dfed;
    --stripe:#3f7fcc;
    --bark:#5a3a22;
    --ink:#2f2a26;
    --backdrop:#e8f0f7;
    --lawn:#6f9a4a;
    --lawn-dark:#4d7335;
    --timber:#c9a57a;
    --timber-dark:#9c7a52;
    --iron:#3d4a3a;
    --shed:#e6e0d2;
    --brick:#b06b55;
  }
  *{box-sizing:border-box;margin:0;padding:0}
  html,body{width:1200px;height:555px;overflow:hidden}
  body{background:var(--backdrop);font-family:"Nunito",sans-serif;color:var(--ink);position:relative}
  .page{position:absolute;top:23px;width:360px;height:508px;background:var(--page);overflow:hidden;box-shadow:0 4px 14px rgba(40,70,110,.25)}
  .page--front{left:232px}
  .page--back{left:608px}
  .corners,.stripes{position:absolute;inset:0;width:100%;height:100%}
  .brand{position:absolute;left:0;right:0;top:22px;text-align:center}
  .brand__name{display:inline-flex;align-items:center;gap:6px;font-family:"Nunito",sans-serif;font-weight:800;font-size:15px;color:var(--bark)}
  .brand__dot{width:10px;height:10px;border-radius:50%;background:var(--sky)}
  .brand__phone{font-weight:800;font-size:13px;color:var(--ink);margin-top:1px}
  .brand__tagline{font-size:5px;font-weight:700;margin-top:1px}
  .intro{position:absolute;left:20px;right:20px;top:75px;font-size:6.4px;line-height:1.45}
  .headline{position:absolute;left:0;right:0;text-align:center;font-family:"Montserrat Alternates",sans-serif;font-weight:700;letter-spacing:-.5px}
  .headline--winter{top:122px;font-size:45px;color:var(--sky)}
  .headline--sale{top:160px;font-size:80px;line-height:1;color:var(--bark)}
  .collage .shot{position:absolute;box-shadow:2px 3px 5px rgba(0,0,0,.35);border:1px solid #fff}
  .shot--iron{background:linear-gradient(180deg,#8fb3c9 0%,#8fb3c9 30%,var(--iron) 31%,var(--iron) 55%,var(--lawn) 56%,var(--lawn-dark) 100%)}
  .shot--wood{background:linear-gradient(180deg,#9fc1d4 0%,var(--timber) 20%,var(--timber-dark) 80%,var(--lawn) 81%,var(--lawn-dark) 100%)}
  .shot--shed{background:linear-gradient(180deg,#7ea35a 0%,var(--shed) 25%,#cfc8b6 85%,var(--lawn) 86%)}
  .shot--brick{background:linear-gradient(180deg,#b5cfdf 0%,var(--brick) 25%,#8f5444 85%,var(--lawn) 86%)}
  .shot--yard{background:linear-gradient(180deg,#a6c7dc 0%,#7ea35a 35%,var(--lawn-dark) 100%)}
  .back-title{position:absolute;left:0;right:0;text-align:center;font-family:"Montserrat Alternates",sans-serif;font-weight:700}
  .back-title--main{top:12px;font-size:23px;color:var(--bark)}
  .back-title--sub{top:42px;font-size:23px;color:var(--sky)}
  .back-copy{position:absolute;left:28px;right:28px;font-size:6.6px;line-height:1.4}
  .back-copy--lead{top:80px}
  .back-copy--services{top:138px;left:30px;font-size:7px;line-height:1.3}
  .section-title{position:absolute;left:0;right:0;top:116px;text-align:center;font-family:"Montserrat Alternates",sans-serif;font-weight:600;font-size:17px;color:#4a4a4a}
  .feature{position:absolute;top:178px;width:146px;height:86px;border:1px solid #fff}
  .feature--aluminum{left:28px}
  .feature--wood{left:186px}
  .feature__tag{position:absolute;right:6px;bottom:8px;padding:2px 7px;border:1px solid #fff;background:rgba(255,255,255,.25);color:#fff;font-family:"Montserrat Alternates",sans-serif;font-style:italic;font-size:8.5px;line-height:1.05;text-align:center;transform:rotate(-14deg)}
  .feature-copy{position:absolute;top:293px;width:148px;font-size:6.8px;line-height:1.4}
  .feature-copy--aluminum{left:28px}
  .feature-copy--wood{left:186px}
  .style-grid{position:absolute;left:28px;top:338px;display:grid;grid-template-columns:58px 58px;column-gap:8px;row-gap:3px}
  .style-card__img{width:58px;height:50px;border:1px solid #fff}
  .style-card__name{font-weight:800;font-size:6.8px;line-height:1.15;margin-top:2px;text-transform:uppercase}
  .catalog{position:absolute;left:186px;top:336px;width:160px}
  .catalog__group{position:absolute}
  .catalog__label{font-weight:700;font-size:5.3px;text-transform:uppercase;line-height:1.2;color:#3a3a3a}
  .catalog__row{display:flex;gap:2px;margin-top:2px}
  .catalog__item{width:22px}
  .catalog__thumb{width:22px;height:18px;border:1px solid #fff}
  .catalog__caption{font-size:2.6px;line-height:1.2;margin-top:1px;white-space:nowrap}
</style>
</head>
<body>

<article class="page page--front">
  <svg class="stripes" viewBox="0 0 360 508" aria-hidden="true">
    <path d="M360 238 C330 300 300 360 250 420 L262 424 C312 366 342 306 360 258 Z" fill="var(--stripe)"/>
    <path d="M360 270 C338 330 310 390 270 440 L282 444 C322 394 348 336 360 292 Z" fill="var(--stripe)"/>
    <path d="M0 425 L70 404 L72 416 L0 440 Z" fill="var(--stripe)"/>
    <path d="M0 455 L60 438 L62 448 L0 468 Z" fill="var(--stripe)"/>
  </svg>
  <svg class="corners" viewBox="0 0 360 508" aria-hidden="true">
    <path d="M0 0 H26 L0 24 Z" fill="var(--sky)"/>
    <path d="M360 508 H330 L360 482 Z" fill="var(--bark)"/>
  </svg>

  <header class="brand">
    <div class="brand__name"><span class="brand__dot"></span>Bramblewood Rails</div>
    <div class="brand__phone">555-014-2277</div>
    <div class="brand__tagline">"Because Good Fences Make Good Neighbors"</div>
  </header>

  <p class="intro">Bramblewood Rails consists of a growing team of individuals with over 30 years of experience within the fencing industry. Each member of our staff is well-trained and knowledgeable within their own specialty. All of our installers take pride in the work completed. In our eyes, we are only as successful as the completion of your job – each job is important to us and we strive to give you the best installation experience possible.</p>

  <h1 class="headline headline--winter">Winter Fence</h1>
  <div class="headline headline--sale">sale</div>

  <div class="collage">
    <div class="shot shot--iron" style="left:30px;top:262px;width:128px;height:70px" role="img" aria-label="Photo of a black aluminum fence with arched gate in a backyard"></div>
    <div class="shot shot--wood" style="left:150px;top:256px;width:132px;height:66px" role="img" aria-label="Photo of a wooden shadowbox fence gate"></div>
    <div class="shot shot--iron" style="left:278px;top:278px;width:62px;height:48px" role="img" aria-label="Photo of a black aluminum fence beside a house"></div>
    <div class="shot shot--wood" style="left:88px;top:332px;width:62px;height:48px" role="img" aria-label="Photo of a wooden fence enclosure"></div>
    <div class="shot shot--wood" style="left:150px;top:318px;width:120px;height:88px" role="img" aria-label="Photo of a scalloped wooden privacy fence along a lawn"></div>
    <div class="shot shot--shed" style="left:240px;top:332px;width:92px;height:68px" role="img" aria-label="Photo of a white wooden fence enclosure around equipment"></div>
    <div class="shot shot--iron" style="left:28px;top:385px;width:124px;height:48px" role="img" aria-label="Photo of a black aluminum fence on a sloped yard"></div>
    <div class="shot shot--brick" style="left:268px;top:404px;width:70px;height:54px" role="img" aria-label="Photo of a stained wooden fence"></div>
    <div class="shot shot--yard" style="left:96px;top:430px;width:110px;height:46px" role="img" aria-label="Photo of a wooden fence around a garden"></div>
    <div class="shot shot--yard" style="left:186px;top:452px;width:72px;height:38px" role="img" aria-label="Photo of a backyard patio with fencing"></div>
  </div>
</article>

<article class="page page--back">
  <svg class="corners" viewBox="0 0 360 508" aria-hidden="true">
    <path d="M360 0 H334 L360 24 Z" fill="var(--sky)"/>
    <path d="M0 508 H30 L0 482 Z" fill="var(--bark)"/>
  </svg>

  <h2 class="back-title back-title--main">Best Fence Types</h2>
  <div class="back-title back-title--sub">for Family, Kids &amp; Pets</div>

  <p class="back-copy back-copy--lead">When it comes to selecting the best fence types for animals, family, kids, and pets; there is no lack of choices to make. Between gates, picket width, rail length, and everything in-between, it can be difficult to know where to begin. But whenever you ponder about how to use your yard.</p>

  <h3 class="section-title">Our Services</h3>
  <p class="back-copy back-copy--services">We have been building aluminum fences for decades.<br>You can choose among the flat top, spear top, flat top with spears or staggered spear top fence styles. See the full list of aluminum fence styles below and click on one to see the photo gallery.</p>

  <div class="feature feature--aluminum shot--iron" role="img" aria-label="Photo of a black aluminum fence in a wooded backyard">
    <span class="feature__tag">Aluminum<br>Fences</span>
  </div>
  <div class="feature feature--wood shot--wood" role="img" aria-label="Photo of a long wooden shadowbox fence in a sunny yard">
    <span class="feature__tag">Wood<br>Fences</span>
  </div>

  <p class="feature-copy feature-copy--aluminum">We have been building aluminum fences for decades. You can choose among the flat top, spear top, flat top with spears or staggered spear top fence styles.</p>
  <p class="feature-copy feature-copy--wood">You can choose from a variety of wood fences. Whether you are looking for a privacy fence or something with estate or split rails, you've come to the right place.</p>

  <div class="style-grid">
    <div class="style-card"><div class="style-card__img shot--iron" role="img" aria-label="Flat top aluminum fence photo"></div><div class="style-card__name">Flat Top</div></div>
    <div class="style-card"><div class="style-card__img shot--iron" role="img" aria-label="Spear top aluminum fence photo"></div><div class="style-card__name">Spear Top</div></div>
    <div class="style-card"><div class="style-card__img shot--iron" role="img" aria-label="Flat top with spears aluminum fence photo"></div><div class="style-card__name">Flat Top<br>With<br>Spears</div></div>
    <div class="style-card"><div class="style-card__img shot--iron" role="img" aria-label="Staggered spear aluminum fence photo"></div><div class="style-card__name">Staggered<br>Spear</div></div>
  </div>

  <div class="catalog">
    <div class="catalog__group" style="left:0;top:0">
      <div class="catalog__label">Privacy Wood Fences</div>
      <div class="catalog__row">
        <div class="catalog__item"><div class="catalog__thumb shot--wood" role="img" aria-label="Dog ear privacy fence photo"></div><div class="catalog__caption">Dog Ear</div></div>
        <div class="catalog__item"><div class="catalog__thumb shot--wood" role="img" aria-label="Gothic top privacy fence photo"></div><div class="catalog__caption">Gothic Top</div></div>
        <div class="catalog__item"><div class="catalog__thumb shot--wood" role="img" aria-label="Scallop privacy fence photo"></div><div class="catalog__caption">Scallop</div></div>
        <div class="catalog__item"><div class="catalog__thumb shot--wood" role="img" aria-label="Flat top privacy fence photo"></div><div class="catalog__caption">Flat Top</div></div>
      </div>
    </div>
    <div class="catalog__group" style="left:122px;top:0">
      <div class="catalog__label">Semi-Privacy<br>Wood Fences</div>
      <div class="catalog__row">
        <div class="catalog__item"><div class="catalog__thumb shot--wood" role="img" aria-label="Shadowbox semi-privacy fence photo"></div><div class="catalog__caption">Shadowbox</div></div>
      </div>
    </div>
    <div class="catalog__group" style="left:0;top:40px">
      <div class="catalog__label">Picket Wood Fences</div>
      <div class="catalog__row">
        <div class="catalog__item"><div class="catalog__thumb shot--wood" role="img" aria-label="Dog ear picket fence photo"></div><div class="catalog__caption">Dog Ear</div></div>
        <div class="catalog__item"><div class="catalog__thumb shot--wood" role="img" aria-label="Gothic picket fence photo"></div><div class="catalog__caption">Gothic</div></div>
        <div class="catalog__item"><div class="catalog__thumb shot--wood" role="img" aria-label="Scallop picket fence photo"></div><div class="catalog__caption">Scallop</div></div>
        <div class="catalog__item"><div class="catalog__thumb shot--wood" role="img" aria-label="French picket fence photo"></div><div class="catalog__caption">French</div></div>
      </div>
    </div>
    <div class="catalog__group" style="left:122px;top:40px">
      <div class="catalog__label">Fences With<br>French Gothic<br>Posts</div>
      <div class="catalog__row">
        <div class="catalog__item"><div class="catalog__thumb shot--wood" role="img" aria-label="French gothic post fence photo"></div><div class="catalog__caption">French Gothic</div></div>
      </div>
    </div>
    <div class="catalog__group" style="left:0;top:90px">
      <div class="catalog__label">Estate Rail Wood Fences</div>
      <div class="catalog__row">
        <div class="catalog__item"><div class="catalog__thumb shot--yard" role="img" aria-label="Split rail fence photo"></div><div class="catalog__caption">Split Rail</div></div>
      </div>
    </div>
    <div class="catalog__group" style="left:0;top:130px">
      <div class="catalog__label">Estate Rail Wood Fences</div>
      <div class="catalog__row">
        <div class="catalog__item"><div class="catalog__thumb shot--yard" role="img" aria-label="Split rail estate fence photo"></div><div class="catalog__caption">Split Rail</div></div>
        <div class="catalog__item"><div class="catalog__thumb shot--yard" role="img" aria-label="Board rail estate fence photo"></div><div class="catalog__caption">Board Rail</div></div>
      </div>
    </div>
  </div>
</article>

</body>
</html>
```